Fitness Business Card Design Needed

We are looking for a business card design that stands out but is also simple and unique. I like the idea of on one side using the picture of myself with my logo at my feet. I love the texture on the business card so please take that into account when designing. Then on the other side having my contact details. I want it to be clean, modern, and pretty. I am open to designs that allow spot gloss or gold foiling.

Space for Name, Phone number, email, and website

```html
<!DOCTYPE html>
<html lang="en">
<head>
<meta charset="utf-8">
<title>PetitePower Fitness – Business Card</title>
<link rel="stylesheet" href="https://fonts.googleapis.com/css2?family=Montserrat:wght@300;400;500&display=swap">
<style>
  :root {
    --canvas: #8e8e8e;
    --card: #0b0b0b;
    --gold: #d9a94a;
    --white: #f4f4f4;
    --rule: #555555;
    --photo-top: #b59a86;
    --photo-bottom: #a9735f;
  }
  * { box-sizing: border-box; margin: 0; padding: 0; }
  html, body { width: 1200px; height: 1200px; overflow: hidden; }
  body {
    background: var(--canvas);
    font-family: "Montserrat", sans-serif;
    position: relative;
  }
  .card {
    position: absolute;
    top: 310px;
    width: 370px;
    height: 594px;
    background: var(--card);
    overflow: hidden;
  }
  .card--front { left: 234px; }
  .card--back { left: 646px; width: 364px; text-align: center; }

  .portrait {
    position: absolute;
    left: 156px;
    top: 14px;
    width: 200px;
    height: 580px;
    border-radius: 100px 100px 0 0;
    background: linear-gradient(180deg, var(--photo-top) 0%, var(--photo-bottom) 100%);
    opacity: 0.8;
  }
  .front-mark {
    position: absolute;
    left: 22px;
    top: 470px;
    display: flex;
    align-items: center;
    gap: 8px;
    color: var(--gold);
    font-size: 11px;
    font-weight: 400;
    letter-spacing: 1.5px;
    white-space: nowrap;
  }
  .mark-square {
    width: 18px;
    height: 18px;
    border: 1.5px solid var(--gold);
  }

  .brand-square {
    position: absolute;
    left: 132px;
    top: 72px;
    width: 100px;
    height: 100px;
    border: 2px solid var(--gold);
  }
  .brand-name {
    position: absolute;
    top: 220px;
    width: 100%;
    color: var(--white);
    font-weight: 300;
    font-size: 25px;
    letter-spacing: 2.5px;
    line-height: 1.3;
  }
  .brand-tagline {
    position: absolute;
    top: 250px;
    left: 54px;
    width: 256px;
    display: flex;
    align-items: center;
    gap: 10px;
    color: var(--gold);
    font-size: 12px;
    font-weight: 400;
    letter-spacing: 6px;
  }
  .brand-tagline::before,
  .brand-tagline::after {
    content: "";
    flex: 1;
    height: 1px;
    background: var(--gold);
  }
  .person-name {
    position: absolute;
    top: 376px;
    width: 100%;
    color: var(--gold);
    font-size: 22px;
    font-weight: 400;
  }
  .person-role {
    position: absolute;
    top: 402px;
    width: 100%;
    color: var(--white);
    font-size: 16px;
    font-weight: 400;
  }
  .contact-icons {
    position: absolute;
    top: 441px;
    left: 87px;
  }
  .contact-list {
    position: absolute;
    top: 476px;
    width: 100%;
    list-style: none;
    color: var(--white);
    font-size: 16px;
    line-height: 21.5px;
  }
</style>
</head>
<body>
  <section class="card card--front">
    <div class="portrait" role="img" aria-label="Full-length photo of the trainer standing, hands on hips"></div>
    <div class="front-mark"><div class="mark-square"></div>PETITEPOWER</div>
  </section>

  <section class="card card--back">
    <div class="brand-square"></div>
    <h1 class="brand-name">PETITEPOWER</h1>
    <p class="brand-tagline">FITNESS</p>
    <p class="person-name">DANIEL REED</p>
    <p class="person-role">MANAGING DIRECTOR</p>
    <svg class="contact-icons" width="190" height="24" viewBox="0 0 190 24" aria-hidden="true">
      <line x1="0" y1="12" x2="52" y2="12" stroke="#555" stroke-width="1"/>
      <line x1="138" y1="12" x2="190" y2="12" stroke="#555" stroke-width="1"/>
      <circle cx="67" cy="12" r="11" fill="var(--gold)"/>
      <circle cx="95" cy="12" r="11" fill="var(--gold)"/>
      <circle cx="123" cy="12" r="11" fill="var(--gold)"/>
      <path d="M61 9 q6 -4 12 0 l-1 2 h-2 l-1 -1.5 h-4 l-1 1.5 h-2 z M62 12 h10 v4 h-10 z" fill="#fff"/>
      <rect x="89" y="8" width="12" height="8" fill="#fff"/>
      <path d="M89 8 l6 5 l6 -5" fill="none" stroke="var(--gold)" stroke-width="1"/>
      <circle cx="123" cy="12" r="6" fill="#fff"/>
      <path d="M117 12 h12 M123 6 v12" stroke="var(--gold)" stroke-width="1"/>
    </svg>
    <ul class="contact-list">
      <li>055-987 654 321</li>
      <li>HELLO@PETITEPOWER.COM</li>
      <li>WWW.PETITEPOWER.COM</li>
    </ul>
  </section>
</body>
</html>
```